KELPMARROW, LLC needs a hybrid app to evaluate and develop athletes

KELPMARROW, LLC needs initial hybrid mobile app and website holding page. KELPMARROW, LLC allows athletes to develop their skills (soccer is initial sport) for free. Receive daily/weekly reminders. Access training videos. Earn points to "upgrade" their soccer profile in "app soccer store". See their points/rankings compared to all app users. Progress streak. This free app (for athletes) will communicate to paid app (coaches) in the future. We would like to see designs use the color blue. The design will communicate health and wellness.

```html
<!DOCTYPE html>
<html lang="en">
<head>
<meta charset="utf-8">
<title>KELPMARROW — Athlete Login &amp; Create Account</title>
<link rel="stylesheet" href="https://fonts.googleapis.com/css2?family=Oxanium:wght@300;400&family=Open+Sans:wght@300;600&display=swap">
<style>
  :root {
    --page: #ffffff;
    --card: #fdfdfd;
    --brand-blue: #0b4fa0;
    --accent-blue: #3578b8;
    --bar-blue: #86a9d2;
    --placeholder: #c9ccd0;
    --glow: rgba(60, 120, 200, 0.38);
    --button-shadow: rgba(0, 0, 0, 0.12);
  }
  * { box-sizing: border-box; margin: 0; padding: 0; }
  html, body {
    width: 1200px; height: 1200px; overflow: hidden;
    background: var(--page);
  }
  .canvas { position: relative; width: 1200px; height: 1200px; }

  .screen {
    position: absolute; top: 203px; width: 454px; height: 801px;
    background: var(--card);
    box-shadow: 0 0 14px 2px var(--glow);
  }
  .screen--login { left: 103px; }
  .screen--signup { left: 650px; }

  .wordmark {
    position: absolute; left: 0; width: 100%; text-align: center;
    font-family: "Oxanium", sans-serif; font-weight: 300;
    font-size: 37px; letter-spacing: 7px; color: var(--brand-blue);
    line-height: 1;
  }
  .screen--login .wordmark { top: 406px; }
  .screen--signup .wordmark { top: 266px; }
  .screen .wordmark { top: auto; }
  .screen--login .wordmark { top: 206px; }
  .screen--signup .wordmark { top: 66px; }

  .heading {
    position: absolute; left: 0; width: 100%; text-align: center;
    font-family: "Oxanium", sans-serif; font-weight: 400;
    color: var(--accent-blue); line-height: 1;
  }
  .heading--login { top: 433px; font-size: 33px; letter-spacing: 1px; }
  .heading--signup { top: 178px; font-size: 35px; letter-spacing: 1px; }

  .field {
    position: absolute; height: 37px;
    border-bottom: 3px solid var(--accent-blue);
    font-family: "Open Sans", sans-serif; color: var(--placeholder);
    text-align: center;
  }
  .field::before, .field::after {
    content: ""; position: absolute; bottom: 4px; width: 3px; height: 31px;
    background: var(--bar-blue);
  }
  .field::before { left: 1px; }

  .field--login { left: 34px; width: 254px; font-weight: 600; font-size: 20px; line-height: 34px; }
  .field--login::after { display: none; }
  .field--username { top: 521px; }
  .field--password { top: 589px; }

  .field--signup { left: 100px; width: 254px; font-weight: 300; font-size: 20px; line-height: 32px; }
  .field--signup::after { right: 1px; }
  .field--1 { top: 262px; }
  .field--2 { top: 331px; }
  .field--3 { top: 398px; }
  .field--4 { top: 466px; }
  .field--5 { top: 533px; }

  .button {
    position: absolute; width: 112px; height: 46px; border-radius: 3px;
    font-family: "Open Sans", sans-serif; font-weight: 600; font-size: 20px;
    line-height: 44px; text-align: center;
  }
  .button--outline {
    background: #fff; color: var(--accent-blue);
    box-shadow: 0 0 3px var(--button-shadow);
  }
  .button--filled { background: var(--accent-blue); color: #fff; }
  .button--login { left: 321px; top: 511px; }
  .button--signup-small { left: 321px; top: 580px; }
  .button--signup-main { left: 172px; top: 639px; color: var(--brand-blue); }

  .copyright {
    position: absolute; left: 0; top: 757px; width: 100%; text-align: center;
    font-family: "Oxanium", sans-serif; font-weight: 300;
    font-size: 16px; letter-spacing: 1px; color: var(--brand-blue);
  }
</style>
</head>
<body>
<main class="canvas">
  <section class="screen screen--login">
    <div class="wordmark">KELPMARROW</div>
    <h1 class="heading heading--login">ATHLETE LOGIN</h1>
    <div class="field field--login field--username">Username</div>
    <div class="field field--login field--password">Password</div>
    <div class="button button--outline button--login">Login</div>
    <div class="button button--filled button--signup-small">Signup</div>
    <p class="copyright">© Copyright&nbsp; 2020&nbsp; KELPMARROW, LLC</p>
  </section>

  <section class="screen screen--signup">
    <div class="wordmark">KELPMARROW</div>
    <h1 class="heading heading--signup">Create Account</h1>
    <div class="field field--signup field--1">Username</div>
    <div class="field field--signup field--2">Age</div>
    <div class="field field--signup field--3">Gender</div>
    <div class="field field--signup field--4">Country</div>
    <div class="field field--signup field--5">State/Zip</div>
    <div class="button button--outline button--signup-main">Signup</div>
    <p class="copyright">© Copyright&nbsp; 2020&nbsp; KELPMARROW, LLC</p>
  </section>
</main>
</body>
</html>
```